TerraLume Business Card Design Project

We need a business card design for a new company called "TerraLume Systems". TerraLume provides 3D visualization software for subsurface oil and gas data so you can make confident downhole decisions.

Our goal is to provide easy to understand big pictures of your data so your can make confident planning decisions.

Our tagline is
SEAMLESS DATA SHARING. EFFECTIVE COLLABORATION. CONFIDENT DECISION-MAKING

Check out http://www.terralume-example.com for more ideas.

The design should promote a technology company that delivers web-based solutions focused on photo-realistic 3D graphics.

The colors from our existing logo (attached) are one option but not a requirement. The design SHOULD NOT use the existing logo.

The design should be two sided and full color. If you require any special print considerations (example: paper type, matte finish, metallic ink, etc) please provide detailed comments. Please also specify any desired details such as rounding of corners, etc.

IF YOU USE BLACK our printer states "We recommend using CMYK black (0, 0, 0, 100) or for a rich black (60, 40, 40, 100). Ensure your artwork is in CMYK mode before adjusting the black."

For design purposes you can use the following contact information

name: Harlan Pike
title: founder
phone: 555.987.6543
email: harlan@terralume-example.com

company information
TerraLume is our "branded" name
"TerraLume Systems" is our official name
www.terralume-example.com

address:
Suite 720
482 Birchmont Avenue SW
Calgary, AB, Canada
T3K 4R8

Target Market(s)

Companies spend a lot of time collecting, organizing and analyzing data but it's really hard to to get a big picture view of current and planned projects, especially in context to existing wellbores, geology and downhole equipment

TerraLume enables you to explore the big picture in an immersive, 3D environment. Our goal is to help transform you rich data into an easily understood picture, to make confident planning decisions and anticipate trouble events before the expensive execution phase.

Industry/Entity Type

Oil And Gas

Requirements
Must have
• The business card design should be sized to a standard 3.5 x 2 inches and print ready. See the attachment for a sample sized card
It MUST meet these requirements:
Exported as PDF file with two pages:
page 1: front design
page 2: back design
All Images must be 300ppi or higher (at 100%)
CMYK colour mode
0.125 inches of bleed on all sides (0.25 inches additional width and height)
0.125 inch safety margin (inside trim line)

```html
<!DOCTYPE html>
<html lang="en">
<head>
<meta charset="utf-8">
<title>TerraLume Systems – Business Card</title>
<link rel="stylesheet" href="https://fonts.googleapis.com/css2?family=Arimo:wght@400;700&family=Open+Sans:wght@800&display=swap">
<style>
  :root {
    --leaf-green: #8dc63f;
    --deep-green: #5f8a2a;
    --mid-green: #76a838;
    --berry: #9b1b3a;
    --paper: #ffffff;
    --trim: #000000;
  }
  * { margin: 0; padding: 0; box-sizing: border-box; }
  html, body {
    width: 1200px;
    height: 1000px;
    overflow: hidden;
    background: var(--paper);
  }
  .sheet { position: relative; width: 1200px; height: 1000px; }

  .card {
    position: absolute;
    border: 1px solid var(--trim);
    overflow: hidden;
    background: var(--paper);
  }

  /* Front */
  .card-front { left: 96px; top: 41px; width: 495px; height: 865px; }
  .brand-zone {
    position: absolute; left: 0; top: 0; width: 100%; height: 367px;
    display: flex; align-items: center; justify-content: center;
  }
  .brand-name {
    font-family: "Arimo", Arial, sans-serif;
    font-weight: 400;
    font-size: 66px;
    color: var(--leaf-green);
    letter-spacing: 0.5px;
    margin-top: 60px;
  }
  .contact-zone {
    position: absolute; left: 0; top: 367px; width: 100%; height: 498px;
    background: var(--leaf-green);
    color: var(--berry);
    font-family: "Arimo", Arial, sans-serif;
    font-weight: 700;
    text-align: center;
  }
  .person-name { position: absolute; width: 100%; top: 58px; font-size: 50px; line-height: 1; }
  .person-title { position: absolute; width: 100%; top: 132px; font-size: 34px; line-height: 1; }
  .contact-line { position: absolute; width: 100%; line-height: 1; white-space: nowrap; }
  .phone { top: 253px; font-size: 28px; }
  .email { top: 315px; font-size: 23px; }
  .web { top: 353px; font-size: 24px; }
  .address-1 { top: 409px; font-size: 24px; }
  .address-2 { top: 449px; font-size: 24px; }

  /* Back */
  .card-back { left: 639px; top: 41px; width: 492px; height: 860px; }
  .back-art { position: absolute; inset: 0; width: 100%; height: 100%; }
  .headline-art {
    position: absolute;
    left: 5px; top: 140px;
    width: 380px; height: 170px;
    border-radius: 24px;
    background: linear-gradient(160deg, var(--leaf-green) 0%, var(--mid-green) 55%, var(--deep-green) 100%);
    transform: rotate(-57deg);
  }
  .tagline {
    position: absolute;
    font-family: "Open Sans", Arial, sans-serif;
    font-weight: 800;
    color: var(--paper);
    line-height: 1;
    white-space: nowrap;
    text-align: center;
    transform: translate(-50%, -50%) rotate(-58.5deg);
  }
  .tagline-primary { left: 248px; top: 560px; font-size: 77px; }
  .tagline-secondary { left: 342px; top: 615px; font-size: 77px; }
</style>
</head>
<body>
<main class="sheet">

  <section class="card card-front" aria-label="Business card front">
    <div class="brand-zone">
      <span class="brand-name">TerraLume</span>
    </div>
    <div class="contact-zone">
      <p class="person-name">Harlan Pike</p>
      <p class="person-title">founder</p>
      <p class="contact-line phone">Phone: (555) 987-6543</p>
      <p class="contact-line email">Email: harlan@terralume-example.com</p>
      <p class="contact-line web">www.terralume-example.com</p>
      <p class="contact-line address-1">Suite 720 482 Birchmont Avenue SW</p>
      <p class="contact-line address-2">Calgary, AB, Canada T3K 4R8</p>
    </div>
  </section>

  <section class="card card-back" aria-label="Business card back">
    <svg class="back-art" viewBox="0 0 492 860" preserveAspectRatio="none" aria-hidden="true">
      <polygon points="492,0 492,860 0,860" fill="var(--leaf-green)"/>
    </svg>
    <div class="headline-art" role="img" aria-label="Extruded green 3D lettering illustration"></div>
    <p class="tagline tagline-primary">VISUALIZATION</p>
    <p class="tagline tagline-secondary">SOFTWARE</p>
  </section>

</main>
</body>
</html>
```